Company website for an international IT business

We require a website for our business, Corvell Solutions. The business has two primary areas: Horizons, which includes two machine learning/deep learning based products and IT consultancy, which is the service we provide to other businesses.

We bridge cutting-edge research to market.

STYLING:
The site can be on single page or multi-page. This is fully open to suggestion. So long as the look and feel are consistent. Currently, we have no strong preference for colors, styles or layouts.
You can find the logo of our website in the attachment “Corvell-logo.png” and “Corvell-logo-landscape.png”.

CONTENT:
You can find the text of the website in “Website-Content.pdf”, which explains the services and products of our business. The format of the text is also open to suggestion - including breaking up the text into visually appealing sections.
We would also like to include suitable images on the website so that it does not appear to be a text-heavy page. We are happy to have placeholder images on stock image sites if needed. We are open to suggestions on placing of images

ATTACHMENT:

Industry/Entity Type

It Company

Coding

Coded - Design and coding required

Number of Pages Required

1 page

Colors

Designer to choose colors to be used in the design.

Requirements
Must have
• A full description of the requirement is in the attachment "Website-Content.pdf"
• The design must have HTML/CSS, and all resources relevant (images, fonts etc)
• We are
Nice to have
• We are open to suggestions on top of the requirement, please reach out and communicate.

```html
<!DOCTYPE html>
<html lang="en">
<head>
<meta charset="utf-8">
<title>Corvell Horizons</title>
<link href="https://fonts.googleapis.com/css2?family=Dosis:wght@300;400;500;600;700;800&display=swap" rel="stylesheet">
<style>
:root{
  --navy-dark:#0d2a55;
  --navy:#102c77;
  --navy-mid:#163a8a;
  --accent:#0a87c6;
  --white:#ffffff;
  --band:#e8e9ec;
  --ink:#2a2a2a;
  --ink-soft:#3c3c3c;
  --link-blue:#1b3a8a;
  --panel:#333333;
  --photo:#8a7f78;
}
*{margin:0;padding:0;box-sizing:border-box}
html,body{width:1200px;height:1174px;overflow:hidden;background:var(--white)}
body{font-family:'Dosis',sans-serif;color:var(--ink);position:relative}
.hero{position:absolute;left:0;top:0;width:1200px;height:628px;overflow:hidden}
.hero-backdrop{position:absolute;inset:0;background:
  radial-gradient(ellipse 420px 360px at 840px 330px,rgba(40,80,170,.35),transparent 70%),
  linear-gradient(90deg,var(--navy-dark) 0%,#10306a 35%,var(--navy) 70%,var(--navy-mid) 100%)}
.brand{position:absolute;left:120px;top:32px;width:110px;text-align:center}
.brand-mark{width:76px;height:76px;border-radius:50%;background:var(--accent);margin:0 auto}
.brand-name{margin-top:6px;color:var(--white);font-weight:700;font-size:22px;letter-spacing:2px;line-height:1}
.social{position:absolute;top:32px;left:900px;display:flex;gap:15px}
.social span{width:24px;height:24px;border-radius:50%;background:var(--white)}
.nav{position:absolute;top:76px;left:0;width:1200px;height:16px}
.nav a{position:absolute;transform:translateX(-50%);color:var(--white);text-decoration:none;font-weight:700;font-size:11.5px;letter-spacing:.2px;white-space:nowrap}
.hero-title{position:absolute;top:240px;left:0;width:1200px;text-align:center;color:var(--white);font-weight:700;font-size:50px;line-height:1;letter-spacing:.5px}
.hero-sub{position:absolute;top:310px;left:0;width:1200px;text-align:center;color:var(--white);font-weight:700;font-size:18.5px;letter-spacing:.1px}
.tour-btn{position:absolute;left:494px;top:386px;width:214px;height:52px;border-radius:4px;background:var(--accent);color:var(--white);font-size:19px;font-weight:500;display:flex;align-items:center;justify-content:center}
.band-top{position:absolute;left:0;top:628px;width:1200px;height:24px;background:var(--band)}
.band-bottom{position:absolute;left:0;top:1154px;width:1200px;height:20px;background:var(--band)}
.welcome-title{position:absolute;top:670px;left:0;width:1242px;text-align:center;font-size:25px;font-weight:400;color:var(--ink)}
.welcome-title em{font-style:normal;color:var(--link-blue)}
.about{position:absolute;left:134px;top:722px;width:480px}
.about h3,.diff h3{font-size:14.5px;font-weight:600;color:var(--ink);margin-bottom:6px}
.about p{font-size:12.5px;font-weight:400;line-height:24px;color:var(--ink-soft)}
.diff{position:absolute;left:858px;top:722px;width:240px}
.diff li{list-style:none;display:flex;align-items:center;gap:8px;height:27.5px;font-size:13px;font-weight:500;color:var(--ink-soft)}
.diff svg{flex:none}
.testimonials-title{position:absolute;top:902px;left:0;width:1200px;text-align:center;font-size:20px;font-weight:400;color:var(--ink);word-spacing:3px}
.testimonial{position:absolute;left:136px;top:950px;width:928px;height:160px;border-radius:6px;background:var(--panel)}
.client-photo{position:absolute;left:17px;top:24px;width:99px;height:79px;background:linear-gradient(135deg,#a39a92,var(--photo) 55%,#5e554f)}
.quote{position:absolute;left:139px;top:20px;width:770px;color:var(--white);font-size:10.5px;line-height:24px;font-weight:400}
.dots{position:absolute;left:442px;top:126px;display:flex;gap:6px}
.dots span{width:11px;height:11px;border-radius:50%;border:1.5px solid var(--white)}
.dots span.active{background:radial-gradient(circle,var(--white) 0 2px,transparent 2.5px)}
</style>
</head>
<body>
<header class="hero">
  <div class="hero-backdrop" role="img" aria-label="Dark blue background with faint binary digits and a digital human profile"></div>
  <div class="brand">
    <div class="brand-mark"></div>
    <div class="brand-name">CORVELL</div>
  </div>
  <div class="social" aria-label="Social links"><span></span><span></span><span></span><span></span><span></span></div>
  <nav class="nav">
    <a href="#" style="left:715px">HOME</a>
    <a href="#" style="left:792px">PRODUCTS</a>
    <a href="#" style="left:886px">CONSULTANCY</a>
    <a href="#" style="left:971px">ABOUT</a>
    <a href="#" style="left:1052px">CONTACT US</a>
  </nav>
  <h1 class="hero-title">CORVELL HORIZONS</h1>
  <p class="hero-sub">CORVELL HORIZONS HAS DEVELOPED TWO CUTTING EDGE PRODUCTS USING MACHINE LEARNING AND DEEPLEARNING.</p>
  <a class="tour-btn">Quick Tour</a>
</header>
<div class="band-top"></div>

<h2 class="welcome-title">Welcome to <em>Corvell Horizons</em></h2>
<section class="about">
  <h3>What is Corvell</h3>
  <p>Corvell Solutions is an IT consultancy firm with a difference<br>
  We can provide IT expertise for your business at any stage - from initial idea to live systems<br>
  systems focus on external factors such as speed, distance to the vehicle ahead, keeping within<br>
  road</p>
</section>
<section class="diff">
  <h3>How are we different</h3>
  <ul>
    <li><svg width="20" height="20" viewBox="0 0 20 20"><circle cx="10" cy="10" r="9" fill="none" stroke="#1b3a8a" stroke-width="1.5"/><path d="M5.5 10.5l3 3 6-7" fill="none" stroke="#1b3a8a" stroke-width="1.5"/></svg>Project Point Person</li>
    <li><svg width="20" height="20" viewBox="0 0 20 20"><circle cx="10" cy="10" r="9" fill="none" stroke="#1b3a8a" stroke-width="1.5"/><path d="M5.5 10.5l3 3 6-7" fill="none" stroke="#1b3a8a" stroke-width="1.5"/></svg>Responsible and accountable</li>
    <li><svg width="20" height="20" viewBox="0 0 20 20"><circle cx="10" cy="10" r="9" fill="none" stroke="#1b3a8a" stroke-width="1.5"/><path d="M5.5 10.5l3 3 6-7" fill="none" stroke="#1b3a8a" stroke-width="1.5"/></svg>for deliverables and communication</li>
  </ul>
</section>

<h2 class="testimonials-title">Client Testimonials</h2>
<section class="testimonial">
  <div class="client-photo" role="img" aria-label="Portrait photo of a client"></div>
  <p class="quote">VIGIL is a system for HGV/HMT drivers to make every journey safer - safer for the driver and safer to other road users.VIGIL uses advanced deep learning techniques to monitor<br>
  driver behavior in real time insidehe cabin. VIGIL can detect driver distraction (mobile phone usage, smoking, failure to<br>
  focused on the road ahead) and also monitor for classic signs of fatigue. Current ADAS</p>
  <div class="dots"><span class="active"></span><span></span><span></span></div>
</section>
<div class="band-bottom"></div>
</body>
</html>
```